Pivots & Treads .com

This website is simple!!!
Landing page background image should capture the customers attention!!! We will provide a image as a example of what we like. The purpose for this website is to provide customers with a clean easy way to request a quote for industrial casters and wheels by OEM’s as well as maintenance departments worldwide. Please see if you can follow our thought process below.
Customer comes to website, they are invited to Request a Quote by providing us with Manufacturer Name, Manufacturers Part # and quantity needed.
If this is not known the customer will complete will WP conversation format form answering about 10 questions
Or
Look up the part number in one of the 8 to 12 catalogs located in the Flippin Book format on our catalog page, or equal plug in .
When the client request a quote a account page will pop up request The following:
Clients first and last name
Email address
And optional questions
Company name and best contact number.
Once this is complete customer will hit SUBMIT.
The customers request will be in system. A email will be sent to Customer service notifying us the Quote Request has been made.
We will then build a quote for the customer with a good, better and best options. Customers Request a Quote submission may have more than one caster or wheel requested at a time, so website must allow this.
When the customer comes back into website there email address will come up as the account name and request a password be made for them. This will allow them to store quotes in their account for future needs. If quote is older than 30 day the system will trigger a button at the bottom of the quote for resubmit Request for updated quote.
Once customer reviews quote the quote can be Converted to order within the website.
Once Converted the system will send us a email and order will be processed.
We will need a Chat program that will text to CS the questions.
You will need to have high quality graphic design skills on your team.
We have found 2 plugins that would work nicely with our new website Flippin books to showcase our catalogs for customers to research and WPForms conversation forms to complete request for quote form.
Just Ideas:
Very very ghosted caster blueprint in white background but very very ghosted or the icon just idea
We have never had a font used we like
Grayscale every except for rubber on wheels and logo icon
Website should have hamburger menu on left
Website should hav responsive deign
Account head on right side
Has anyone read the brief from top to bottom and the updates, I’m seeing a lot of duplicates of the website I posted in images I want a clean website With lite backgrand with the poly being definite colors on each wheel I added a green yellow and red image has anyone looked at that Just a question?
Went on vacation/holiday

```html
<!DOCTYPE html>
<html lang="en">
<head>
<meta charset="UTF-8">
<title>Request a Quote</title>
<link rel="stylesheet" href="https://fonts.googleapis.com/css2?family=Open+Sans:wght@400;600;700&display=swap">
<style>
  :root {
    --ink: #333333;
    --ink-soft: #4a4a4a;
    --muted: #666666;
    --charcoal: #3a3a3a;
    --white: #ffffff;
    --steel-light: #e2e2e2;
    --steel-mid: #b9b9b9;
    --steel-dark: #7d7d7d;
  }
  * { box-sizing: border-box; margin: 0; padding: 0; }
  html, body {
    width: 1200px;
    height: 1167px;
    overflow: hidden;
    background: var(--white);
    font-family: "Open Sans", Arial, sans-serif;
    color: var(--ink);
  }
  .page { position: relative; width: 1200px; height: 1167px; }

  .site-header {
    position: absolute; top: 0; left: 0; width: 1200px; height: 83px;
    background: var(--white);
    box-shadow: 0 2px 4px rgba(0,0,0,0.12);
    z-index: 3;
  }
  .menu-toggle { position: absolute; left: 17px; top: 47px; width: 26px; height: 18px; }

  .hero-backdrop {
    position: absolute; top: 83px; left: 0; width: 1200px; height: 834px;
    background: linear-gradient(180deg, #f3f3f3 0%, #f8f8f8 60%, #fbfbfb 92%, #ffffff 100%);
  }
  .product-visual {
    position: absolute; left: 686px; top: 376px; width: 404px; height: 384px;
    border-radius: 24px;
    background: radial-gradient(ellipse at 50% 50%,
      var(--steel-mid) 0%, var(--steel-light) 45%, rgba(240,240,240,0.6) 72%, rgba(245,245,245,0) 100%);
  }

  .quote-card {
    position: absolute; left: 87px; top: 162px; width: 479px; height: 586px;
    background: var(--white);
    border-radius: 10px;
    box-shadow: 0 2px 6px rgba(0,0,0,0.12);
    text-align: center;
    z-index: 2;
  }
  .quote-title {
    position: absolute; top: 28px; left: 0; width: 100%;
    font-size: 41px; font-weight: 700; letter-spacing: 0.2px; color: var(--ink);
  }
  .quote-lead {
    position: absolute; top: 93px; left: 0; width: 100%;
    font-size: 16.6px; color: var(--ink-soft);
  }
  .field {
    position: absolute; left: 35.5px; width: 408px; height: 40px;
    border-radius: 20px; background: var(--white);
    box-shadow: 0 2px 5px rgba(0,0,0,0.18);
    font-size: 13.5px; color: var(--muted);
    text-align: left; padding-left: 26px; line-height: 40px;
  }
  .field-manufacturer { top: 137px; }
  .field-part { top: 198px; }
  .field-quantity { top: 259px; }

  .btn {
    position: absolute; height: 41px; border-radius: 21px;
    background: var(--charcoal); color: var(--white);
    font-size: 15px; font-weight: 600; line-height: 41px; text-align: center;
  }
  .btn-submit { left: 148px; top: 319px; width: 182px; }
  .help-text {
    position: absolute; top: 393px; left: 0; width: 100%;
    font-size: 16.7px; line-height: 22.5px; color: var(--ink-soft);
  }
  .btn-assistant { left: 46px; top: 492px; width: 183px; }
  .btn-catalog { left: 250.5px; top: 492px; width: 183px; }

  .site-footer {
    position: absolute; left: 0; top: 979px; width: 1200px; height: 188px;
    background: var(--charcoal);
  }
</style>
</head>
<body>
<div class="page">
  <header class="site-header">
    <svg class="menu-toggle" viewBox="0 0 26 18" aria-label="Menu">
      <rect x="0" y="0" width="26" height="2.4" fill="#666"/>
      <rect x="0" y="7.8" width="26" height="2.4" fill="#666"/>
      <rect x="0" y="15.6" width="26" height="2.4" fill="#666"/>
    </svg>
  </header>

  <div class="hero-backdrop" role="img" aria-label="Faint engineering blueprint drawings of caster parts"></div>
  <div class="product-visual" role="img" aria-label="Photo of a chrome swivel caster with a black and red rubber wheel"></div>

  <section class="quote-card">
    <h1 class="quote-title">Request a Quote</h1>
    <p class="quote-lead">Let us know what you are looking for.</p>
    <div class="field field-manufacturer">Manufacturer Name</div>
    <div class="field field-part">Manufacturer Part Number</div>
    <div class="field field-quantity">Quantity Needed</div>
    <div class="btn btn-submit">Submit Request</div>
    <p class="help-text">Don’t know the information above?<br>No worries! Complete our short survey or look<br>through out catalogs to find what you need.</p>
    <div class="btn btn-assistant">Quote Assistant</div>
    <div class="btn btn-catalog">Parts Catalog</div>
  </section>

  <footer class="site-footer"></footer>
</div>
</body>
</html>
```